Landscape Lighting Product Brochure

You created a flyer for us that was for our Christmas Light training business and we really liked the design.

We want to mimic something with similar colors of the blue and gold. However, it would be for product sales for our landscape lighting product line. We want the products to really be the star of the show on this brochure that will include product photos as well as quick details of each product.

We also want to highlight that these products carry a lifetime warranty and are made of high quality Brass.

These products are going to be marketed to installers so not so much your average home owner.

It should also include our logo and contact information, same as the previous flyer.

Target Market(s)

Installers who are looking to purchase high quality materials

Requirements
Must have
• Must be 1 page with all of our products listed. Must have our logo.
Nice to have
• It would be nice to have a small section of details for each product.

```html
<!DOCTYPE html>
<html lang="en">
<head>
<meta charset="utf-8">
<title>Brightfield Lights – Landscape Lighting Product</title>
<link href="https://fonts.googleapis.com/css2?family=Poppins:wght@400;500;600;700;800&display=swap" rel="stylesheet">
<style>
:root{
  --navy:#0b1a36;
  --blue:#1666d9;
  --gold:#f2b31d;
  --ink:#333333;
  --rule:#3a3a3a;
  --page:#ffffff;
  --backdrop:#f3f3f3;
}
*{margin:0;padding:0;box-sizing:border-box}
html,body{width:1200px;height:2311px;overflow:hidden;background:var(--backdrop);font-family:"Poppins",sans-serif}
.flyer{position:absolute;left:60px;top:390px;width:1080px;height:1531px;background:var(--page);box-shadow:0 10px 40px rgba(0,0,0,.18);overflow:hidden}
.header{position:absolute;left:0;top:0;width:1080px;height:485px}
.band-art{position:absolute;left:0;top:0}
.brand{position:absolute;left:64px;top:70px;display:flex;align-items:center;gap:14px}
.brand-dot{width:34px;height:34px;border-radius:50%;background:var(--gold)}
.brand-name{font-weight:700;font-size:44px;color:var(--blue);letter-spacing:1px;line-height:1}
.headline{position:absolute;left:60px;top:215px;font-weight:800;line-height:.98}
.headline span{display:block}
.headline .l1{font-size:71px;color:#fff}
.headline .l2{font-size:86px;color:var(--gold)}
.headline .l3{font-size:86px;color:#fff}
.catalog{position:absolute;left:56px;top:529px;width:972px}
.card{position:absolute;width:233px}
.card-photo{width:233px;height:140px;background:linear-gradient(180deg,#ebebeb,#dcdcdc)}
.card-label{height:46px;display:flex;align-items:center;justify-content:center;text-align:center;font-weight:700;font-size:17px;line-height:1.05;padding:0 8px}
.card-label.gold{background:var(--gold);color:var(--navy)}
.card-label.blue{background:var(--blue);color:#fff}
.specs{padding:10px 0 0 21px}
.specs dt{font-weight:700;font-size:17px;color:var(--blue);letter-spacing:.3px;margin-top:6px}
.specs dt:first-child{margin-top:0}
.specs dd{font-size:14.5px;color:var(--ink);margin-top:2px}
.specs .red{color:#e02020}.specs .amber{color:var(--gold)}
.v-rule{position:absolute;width:2px;background:var(--rule)}
.h-rule{position:absolute;left:0;top:409px;width:972px;height:2px;background:var(--rule)}
.footer{position:absolute;left:0;top:1374px;width:1080px;height:157px}
.contact-call{position:absolute;left:58px;top:26px;color:#fff;font-weight:700;line-height:1.05}
.contact-call .title{font-size:46px}
.contact-call .phone{font-size:46px;display:flex;align-items:center;gap:12px}
.icon{flex:none;display:block}
.contact-web{position:absolute;left:570px;top:40px;font-size:33px;font-weight:500;color:var(--navy);line-height:1.25}
.contact-web .line{display:flex;align-items:center;gap:16px}
</style>
</head>
<body>
<main class="flyer">
  <header class="header">
    <svg class="band-art" width="1080" height="485" viewBox="0 0 1080 485">
      <rect width="1080" height="485" fill="var(--navy)"/>
      <polygon points="641,0 1080,0 1080,485 641,485 520,250" fill="#3a2c22" role="img" aria-label="Photo of a house at night outlined with red and white lights"/>
      <polyline points="641,0 520,250 641,485" fill="none" stroke="var(--gold)" stroke-width="5"/>
      <rect y="481" width="1080" height="4" fill="var(--gold)"/>
    </svg>
    <div class="brand"><span class="brand-dot"></span><span class="brand-name">Brightfield Lights</span></div>
    <h1 class="headline"><span class="l1">LANDSCAPE</span><span class="l2">LIGHTING</span><span class="l3">PRODUCT</span></h1>
  </header>

  <section class="catalog">
    <div class="v-rule" style="left:240px;top:0;height:812px"></div>
    <div class="v-rule" style="left:485px;top:0;height:812px"></div>
    <div class="v-rule" style="left:731px;top:0;height:812px"></div>
    <div class="h-rule"></div>

    <article class="card" style="left:0;top:0">
      <div class="card-photo" role="img" aria-label="Three LED G4 bulbs"></div>
      <div class="card-label gold">LED G4 (SILICONE<br>OR CERAMIC)</div>
      <dl class="specs"><dt>MATERIALS</dt><dd>Silicone or Ceramic</dd><dt>LED COLOR AVIABLE</dt><dd><span class="red">•</span> Red • Green • Blue <span class="amber">•</span> Amber</dd><dt>WARRANTY</dt><dd>3 years warranty</dd></dl>
    </article>
    <article class="card" style="left:245px;top:0">
      <div class="card-photo" role="img" aria-label="Cast brass up light fixture"></div>
      <div class="card-label blue">UP LIGHT FIXTURES</div>
      <dl class="specs"><dt>MATERIALS</dt><dd>Cast brass</dd><dt>LENS</dt><dd>Clear convex glass lens</dd><dt>WARRANTY</dt><dd>Limited lifetime warranty</dd></dl>
    </article>
    <article class="card" style="left:491px;top:0">
      <div class="card-photo" role="img" aria-label="Die-cast brass up light fixture"></div>
      <div class="card-label gold">UP LIGHT FIXTURES</div>
      <dl class="specs"><dt>MATERIALS</dt><dd>Die-cast brass</dd><dt>LENS</dt><dd>Clear flat glass lens</dd><dt>WARRANTY</dt><dd>Limited lifetime warranty</dd></dl>
    </article>
    <article class="card" style="left:737px;top:0">
      <div class="card-photo" role="img" aria-label="Two in-ground light fixtures"></div>
      <div class="card-label blue">IN GROUND<br>LIGHT FIXTURES</div>
      <dl class="specs"><dt>MATERIALS</dt><dd>Die-cast brass,PVC</dd><dt>LENS</dt><dd>Shock resistant glass lens</dd><dt>WARRANTY</dt><dd>Limited lifetime warranty</dd></dl>
    </article>

    <article class="card" style="left:0;top:454px">
      <div class="card-photo" role="img" aria-label="Path light fixture"></div>
      <div class="card-label gold">PATH LIGHT FIXTURES</div>
      <dl class="specs"><dt>MATERIALS</dt><dd>Silicone or Ceramic</dd><dt>LED COLOR AVIABLE</dt><dd><span class="red">•</span> Red • Green • Blue <span class="amber">•</span> Amber</dd><dt>WARRANTY</dt><dd>3 years warranty</dd></dl>
    </article>
    <article class="card" style="left:245px;top:454px">
      <div class="card-photo" role="img" aria-label="LED MR16 bulb"></div>
      <div class="card-label blue">LED MR 16(6 LED)</div>
      <dl class="specs"><dt>MATERIALS</dt><dd>Silicone or Ceramic</dd><dt>LED COLOR AVIABLE</dt><dd>Red&nbsp;&nbsp; Green&nbsp;&nbsp; Blue&nbsp;&nbsp; Amber</dd><dt>WARRANTY</dt><dd>3 years warranty</dd></dl>
    </article>
    <article class="card" style="left:491px;top:454px">
      <div class="card-photo" role="img" aria-label="LED PAR36 lamp"></div>
      <div class="card-label gold">LED PAR36/AR 111</div>
      <dl class="specs"><dt>MATERIALS</dt><dd>Silicone or Ceramic</dd><dt>LED COLOR AVIABLE</dt><dd>Red&nbsp;&nbsp; Green&nbsp;&nbsp; Blue&nbsp;&nbsp; Amber</dd><dt>WARRANTY</dt><dd>3 years warranty</dd></dl>
    </article>
    <article class="card" style="left:737px;top:454px">
      <div class="card-photo" role="img" aria-label="Three lighting transformers"></div>
      <div class="card-label blue">TRANSFORMARS</div>
      <dl class="specs"><dt>MATERIALS</dt><dd>Silicone or Ceramic</dd><dt>LED COLOR AVIABLE</dt><dd>Red&nbsp;&nbsp; Green&nbsp;&nbsp; Blue&nbsp;&nbsp; Amber</dd><dt>WARRANTY</dt><dd>3 years warranty</dd></dl>
    </article>
  </section>

  <footer class="footer">
    <svg class="band-art" width="1080" height="157" viewBox="0 0 1080 157">
      <polygon points="504,26 1080,26 1080,129 562,129" fill="var(--gold)"/>
      <polygon points="0,0 471,0 547,157 0,157" fill="var(--blue)"/>
    </svg>
    <div class="contact-call">
      <div class="title">GET IN TOUCH</div>
      <div class="phone">
        <svg class="icon" width="30" height="30" viewBox="0 0 24 24" aria-hidden="true"><path fill="#fff" d="M6.6 10.8a15.1 15.1 0 0 0 6.6 6.6l2.2-2.2c.3-.3.7-.4 1-.2 1.1.4 2.3.6 3.6.6.6 0 1 .4 1 1V20c0 .6-.4 1-1 1A17 17 0 0 1 3 4c0-.6.4-1 1-1h3.5c.6 0 1 .4 1 1 0 1.3.2 2.5.6 3.6.1.3 0 .7-.2 1z"/></svg>
        <span>555-214-0000</span>
      </div>
    </div>
    <div class="contact-web">
      <div class="line"><svg class="icon" width="30" height="24" viewBox="0 0 30 24" aria-hidden="true"><rect x="1" y="2" width="28" height="20" rx="2" fill="var(--navy)"/><path d="M2 4l13 10 13-10" fill="none" stroke="var(--gold)" stroke-width="2.5"/></svg><span>info@brightfieldlights.com</span></div>
      <div class="line"><svg class="icon" width="30" height="30" viewBox="0 0 30 30" aria-hidden="true"><g fill="none" stroke="var(--navy)" stroke-width="2.5"><circle cx="15" cy="15" r="12"/><ellipse cx="15" cy="15" rx="5" ry="12"/><path d="M3 15h24M5 9h20M5 21h20"/></g></svg><span>www.brightfieldlights.com</span></div>
    </div>
  </footer>
</main>
</body>
</html>
```